letterhead design

We have a business card with logo, ink etc and want to develop letterhead that uses the elements of the business card logo.
Must haves...and they should be designed in, not just plopped in :)
Dr. Marla Quint
2817 W Birch Avenue
Fresno, CA 93728
559-555-0137 p
559-555-0182 f
info@ridgemoorchiropractic.com
www.ridgemoorchiropractic.com
www.friendpage.net/ridgemoorchiro
Updates

Rather than just have the logo on the page, is there someway to silkscreen it in the background to fill the page?

Reason: I was out of town for a week.

Industry/Entity Type

Business

Requirements
Nice to have
• I'd like the logo somehow silk screened in the background of the paper as well.

```html
<!DOCTYPE html>
<html lang="en">
<head>
<meta charset="utf-8">
<title>Ridgemoor Chiropractic Letterhead</title>
<link rel="stylesheet" href="https://fonts.googleapis.com/css2?family=Roboto+Slab:wght@700&family=Cabin:wght@400;700&display=swap">
<style>
  :root {
    --canvas: #ffffff;
    --paper: #ffffff;
    --ink: #111111;
    --screen: #e3e3e4;
    --edge: #9a9a9a;
    --shadow: rgba(0, 0, 0, 0.45);
  }
  * { margin: 0; padding: 0; box-sizing: border-box; }
  html, body {
    width: 1200px;
    height: 900px;
    overflow: hidden;
    background: var(--canvas);
  }
  .sheet {
    position: absolute;
    top: 48px;
    width: 568px;
    height: 803px;
    background: var(--paper);
    border: 1px solid var(--edge);
    box-shadow: 3px 3px 3px var(--shadow);
    overflow: hidden;
    color: var(--ink);
  }
  .sheet--slab { left: 24px; font-family: "Roboto Slab", serif; text-transform: uppercase; }
  .sheet--sans { left: 610px; font-family: "Cabin", sans-serif; }

  .silkscreen {
    position: absolute;
    left: -8px;
    top: 560px;
    font-weight: 700;
    font-size: 150px;
    line-height: 1;
    letter-spacing: 2px;
    color: var(--screen);
    white-space: nowrap;
    text-transform: uppercase;
  }
  .sheet--sans .silkscreen { font-size: 160px; left: -6px; top: 552px; }

  .masthead {
    position: absolute;
    left: 34px;
    top: 60px;
    display: flex;
    align-items: flex-start;
  }
  .brand {
    width: 140px;
    font-weight: 700;
    font-size: 20px;
    line-height: 1;
    text-transform: uppercase;
    padding-top: 2px;
  }
  .sheet--sans .brand { font-size: 22px; }
  .contact {
    margin-left: 9px;
    font-size: 7px;
    line-height: 9px;
    white-space: nowrap;
  }
  .sheet--sans .contact { font-size: 8px; }
  .contact .name { font-weight: 700; font-size: 8px; }
  .sheet--sans .contact .name { font-size: 9px; }
  .sheet--sans .contact .line { font-weight: 400; }

  .footer {
    position: absolute;
    left: 34px;
    top: 722px;
    font-size: 7px;
    line-height: 12px;
    font-weight: 700;
    position: absolute;
  }
  .sheet--sans .footer { left: 32px; top: 732px; font-size: 8px; line-height: 10px; font-weight: 700; }
</style>
</head>
<body>
  <section class="sheet sheet--slab" aria-label="Letterhead, slab serif version">
    <div class="silkscreen" aria-hidden="true">Ridgemoor</div>
    <header class="masthead">
      <div class="brand">Ridgemoor</div>
      <div class="contact">
        <div class="name">Dr. Marla Quint</div>
        <div class="line">2817 W Birch Avenue, Fresno, CA 93728</div>
        <div class="line">Phone: 559-555-0137&nbsp;&nbsp; Fax: 559-555-0182</div>
      </div>
    </header>
    <footer class="footer">
      <div>info@ridgemoorchiropractic.com</div>
      <div>www.ridgemoorchiropractic.com</div>
      <div>www.friendpage.net/ridgemoorchiro</div>
    </footer>
  </section>

  <section class="sheet sheet--sans" aria-label="Letterhead, sans serif version">
    <div class="silkscreen" aria-hidden="true">Ridgemoor</div>
    <header class="masthead">
      <div class="brand">Ridgemoor</div>
      <div class="contact">
        <div class="name">Dr. Marla Quint</div>
        <div class="line">2817 W Birch Avenue, Fresno, CA 93728</div>
        <div class="line">Phone: 559-555-0137&nbsp; Fax: 559-555-0182</div>
      </div>
    </header>
    <footer class="footer">
      <div>info@ridgemoorchiropractic.com</div>
      <div>www.ridgemoorchiropractic.com</div>
      <div>www.friendpage.net/ridgemoorchiro</div>
    </footer>
  </section>
</body>
</html>
```